Remake homepage in our website

To redesign the homepage of Datavane's website, highlighting its key solutions: Ferrolith, Joltmesh, and BXN Relay. The goal is to communicate Datavane's value proposition effectively, attract potential clients, and provide an intuitive navigation experience.
Target Audience
Primary Audience: Decision-makers in the industrial sector, including plant managers, automation engineers, and IT managers.
Secondary Audience: Current clients and stakeholders looking to explore new solutions.
Key Messages
Datavane is a leader in connectivity, cybersecurity, and industrial data management solutions.
Ferrolith, Joltmesh, and BXN Relay are innovative tools designed to optimize industrial operations.
Datavane offers personalized support and over two decades of expertise.
Deliverables
Homepage Design:
Hero section with a strong headline, supportive subhead, and prominent CTAs.
Clear presentation of Ferrolith, Joltmesh, and BXN Relay with brief descriptions and links to more details.
Visual elements (e.g., icons, images, videos) that align with the brand's identity.
Sections showcasing Datavane's experience and client testimonials.
Content Development:
Copywriting for each section of the homepage.
Visual assets (e.g., illustrations, photos, and short videos) for product highlights and brand storytelling.
Requirements
Modern and professional design aligned with Datavane's branding.
Intuitive navigation that guides users to key sections and CTAs.
Integration with the existing CMS or website platform.
Testing to ensure responsiveness and functionality across devices.

```html
<!DOCTYPE html>
<html lang="en">
<head>
<meta charset="utf-8">
<title>Datavane — Industrial Connectivity</title>
<link href="https://fonts.googleapis.com/css2?family=Montserrat:wght@400;500;600;700&display=swap" rel="stylesheet">
<style>
:root{
  --blue:#0a7bc2;
  --blue-dark:#075f98;
  --navy:#1a4d86;
  --grey:#8b959c;
  --ink:#111;
  --text:#555;
  --line:#c9c9c9;
  --white:#fff;
  --black:#000;
}
*{margin:0;padding:0;box-sizing:border-box}
html,body{width:1200px;height:3419px;overflow:hidden;background:var(--white)}
body{position:relative;font-family:'Montserrat',sans-serif;color:var(--ink)}
.abs{position:absolute}
a{text-decoration:none;color:inherit}

/* nav */
.brand{position:absolute;left:110px;top:28px;font-size:38px;font-weight:600;color:var(--blue);letter-spacing:.5px}
.nav{position:absolute;top:0;left:0;width:1200px;height:101px}
.nav a{position:absolute;top:40px;font-size:16px;color:#333}
.nav a.active{color:var(--blue)}
.nav .indicator{position:absolute;left:518px;top:0;width:70px;height:4px;background:var(--blue)}

/* hero */
.hero-bg{position:absolute;left:0;top:101px;width:1200px;height:580px;
  background:linear-gradient(90deg,#0f2348 0%,#22355f 45%,#3a4a72 70%,#1c2a4d 100%)}
.hero-cut{position:absolute;left:0;top:590px}
.hero-copy{position:absolute;left:114px;top:243px;border-left:2px solid var(--blue);padding-left:10px;color:var(--white)}
.hero-copy .kicker{font-size:27px;font-weight:400}
.hero-copy h1{font-size:48px;font-weight:600;margin-top:6px;line-height:1.1}
.hero-sub{position:absolute;left:127px;top:346px;width:420px;font-size:16px;line-height:25px;color:#e9eef5}
.btn{position:absolute;height:40px;border-radius:20px;display:flex;align-items:center;gap:8px;padding-left:15px;font-size:14px;color:var(--white)}
.btn.solid{background:var(--blue)}
.btn.ghost{border:1.5px solid var(--white)}
.btn svg{width:26px;height:26px}

/* section heads */
.rule{position:absolute;height:2px;background:var(--blue)}
.sec-title{position:absolute;left:0;width:1200px;text-align:center;font-size:40px;font-weight:600}
.sec-title span{color:var(--blue);font-weight:400}

/* cards */
.card{position:absolute;top:898px;width:318px;height:320px;border:2px solid #d6d6d6;padding:26px 24px}
.card.featured{background:var(--blue);border-color:var(--blue);color:var(--white)}
.card .icon{width:66px;height:66px}
.card h3{font-size:31px;font-weight:700;color:var(--blue);margin-top:22px}
.card.featured h3{color:var(--white)}
.card p{font-size:16px;line-height:25px;color:var(--text);margin-top:12px}
.card.featured p{color:var(--white)}
.card .more{position:absolute;left:24px;top:276px;display:flex;align-items:center;gap:10px;font-size:18px;font-weight:500}
.card .more svg{width:30px;height:30px}

/* why */
.why-bg{position:absolute;left:0;top:1300px}
.why-photo{position:absolute;left:143px;top:1456px;width:397px;height:491px;border-radius:34px;
  background:linear-gradient(160deg,#c9c2b4 0%,#8f8a80 40%,#d98a4a 70%,#4a5a70 100%)}
.why-copy{position:absolute;left:605px;top:1516px;color:var(--white)}
.why-copy .bar{width:146px;height:2px;background:var(--white)}
.why-copy h2{font-size:40px;font-weight:600;margin-top:22px;line-height:47px}
.why-copy h2 span{font-weight:400;display:block}
.why-copy ul{list-style:none;margin-top:26px}
.why-copy li{display:flex;align-items:center;gap:20px;font-size:19px;font-weight:500;height:30px}
.why-copy li svg{width:16px;height:16px;flex:none}

/* testimonial */
.quote-mark{position:absolute;font-family:Georgia,serif;font-size:150px;line-height:1;color:var(--navy);font-weight:700}
.quote-text{position:absolute;left:163px;top:2232px;width:510px;font-size:17px;line-height:26px;color:var(--text)}
.author{position:absolute;left:167px;top:2356px;display:flex;align-items:center;height:52px}
.author .name{font-size:23px;font-weight:600;color:var(--blue);padding-right:12px;border-right:2px solid var(--blue);height:52px;display:flex;align-items:center}
.author .role{font-size:18px;color:#999;padding-left:16px}
.dots{position:absolute;left:167px;top:2424px;display:flex;gap:8px}
.dots i{width:16px;height:16px;border-radius:50%;border:1.5px solid #aaa;display:block}
.dots i.on{background:var(--blue);border-color:var(--blue)}
.portrait-ring{position:absolute;left:714px;top:2132px;width:380px;height:372px;border-radius:50%;background:var(--blue)}
.portrait{position:absolute;left:730px;top:2138px;width:362px;height:362px;border-radius:50%;
  background:radial-gradient(circle at 50% 60%,#6b6f74 0%,#9da2a5 45%,#e6e8e8 80%)}

/* footer */
.foot-bg{position:absolute;left:0;top:2580px}
.cta-copy{position:absolute;left:112px;top:2790px;color:var(--white)}
.cta-copy .bar{width:146px;height:2px;background:var(--white);margin-left:2px}
.cta-copy h2{font-size:41px;font-weight:600;line-height:56px;margin-top:14px}
.cta-copy p{font-size:16px;line-height:29px;width:470px;margin-top:20px;padding-left:2px}
.btn.cta{left:113px;top:3134px;height:42px;width:292px;border-radius:21px;font-size:14px}
.foot-brand{position:absolute;left:118px;top:3242px;font-size:40px;font-weight:600;color:var(--blue)}
.copyright{position:absolute;left:120px;top:3328px;font-size:19px;color:var(--white)}

.form-card{position:absolute;left:660px;top:2720px;width:428px;height:582px;background:var(--white);border-radius:34px}
.form-card h3{position:absolute;top:26px;width:100%;text-align:center;font-size:31px;font-weight:600;color:var(--blue)}
.field{position:absolute;left:25px;width:379px;height:55px;border:1.5px solid #b5b5b5;border-radius:6px;font-size:18px;color:#444;padding:16px 17px}
.form-card .send{position:absolute;left:26px;top:511px;width:376px;height:43px;border-radius:22px;background:var(--blue);color:var(--white);display:flex;justify-content:center;align-items:center;gap:12px;font-size:18px}
.form-card .send svg{width:28px;height:28px}
</style>
</head>
<body>

<header class="nav">
  <div class="brand">Datavane</div>
  <span class="indicator"></span>
  <a class="active" style="left:531px">Home</a>
  <a style="left:626px">Solutions</a>
  <a style="left:747px">Benefits</a>
  <a style="left:859px">Testimonials</a>
  <a style="left:1004px">Contact Us</a>
</header>

<section>
  <div class="hero-bg" role="img" aria-label="Industrial plant at dusk overlaid with a network of connected lines"></div>
  <svg class="hero-cut" width="1200" height="100" viewBox="0 0 1200 100">
    <polygon points="0,92 1046,2 1046,100 0,100" fill="#fff"/>
    <polygon points="0,92 1046,2 1046,27 0,100" fill="var(--blue)"/>
    <polygon points="1046,27 1200,0 1200,100 1046,100" fill="#fff"/>
    <polygon points="862,40 1200,10 1200,86" fill="var(--grey)"/>
  </svg>
  <div class="hero-copy">
    <div class="kicker">Empowering Connectivity and</div>
    <h1>Industrial Efficiency</h1>
  </div>
  <p class="hero-sub">Leading solutions in cybersecurity, connectivity, and data management for Industry 4.0.</p>
  <a class="btn solid" style="left:127px;top:414px;width:210px">Learn About Ferrolith
    <svg viewBox="0 0 26 26" fill="none" stroke="#fff" stroke-width="1.5"><path d="M17 4a10 10 0 1 1 0 18"/><path d="M4 13h15M14 8l5 5-5 5"/></svg></a>
  <a class="btn ghost" style="left:348px;top:414px;width:174px">Explore Joltmesh
    <svg viewBox="0 0 26 26" fill="none" stroke="#fff" stroke-width="1.5"><path d="M17 4a10 10 0 1 1 0 18"/><path d="M4 13h15M14 8l5 5-5 5"/></svg></a>
  <a class="btn ghost" style="left:532px;top:414px;width:195px">Discover BXN Relay
    <svg viewBox="0 0 26 26" fill="none" stroke="#fff" stroke-width="1.5"><path d="M17 4a10 10 0 1 1 0 18"/><path d="M4 13h15M14 8l5 5-5 5"/></svg></a>
</section>

<section>
  <div class="rule" style="left:527px;top:780px;width:146px"></div>
  <h2 class="sec-title" style="top:800px">Solutions That <span>Transform Your Plant</span></h2>

  <article class="card" style="left:111px">
    <svg class="icon" viewBox="0 0 66 66" fill="none" stroke="#222" stroke-width="1.8" stroke-linejoin="round"><path d="M33 34V16"/><path d="M33 22c-6 0-10-4-10-10 6 0 10 4 10 10zM33 22c6 0 10-4 10-10-6 0-10 4-10 10z"/><path d="M6 50l10-10c3-2 6-2 9 0l8 3c2 1 2 4 0 5h-9"/><path d="M24 48l14-2 12-8c2-1 4 1 3 3L40 54l-14 4-12-2"/></svg>
    <h3>Ferrolith</h3>
    <p>"Comprehensive automation management and data backup for uninterrupted industrial operations."</p>
    <a class="more">Learn More <svg viewBox="0 0 30 30" fill="none" stroke="#222" stroke-width="1.5"><path d="M19 4a11 11 0 1 1 0 22"/><path d="M4 15h18M17 10l5 5-5 5"/></svg></a>
  </article>

  <article class="card featured" style="left:442px">
    <svg class="icon" viewBox="0 0 66 66" fill="none" stroke="#fff" stroke-width="1.8"><circle cx="20" cy="24" r="8"/><circle cx="20" cy="24" r="3"/><path d="M20 12v4M20 32v4M8 24h4M28 24h4"/><path d="M36 22l8-8 6 6M44 14l4-4M50 20v10"/><rect x="38" y="30" width="14" height="10"/><rect x="6" y="44" width="52" height="10" rx="5"/><circle cx="14" cy="49" r="2"/><circle cx="26" cy="49" r="2"/><circle cx="38" cy="49" r="2"/><circle cx="50" cy="49" r="2"/></svg>
    <h3>Joltmesh</h3>
    <p>"Reliable connectivity between industrial systems and devices."</p>
    <a class="more">Learn More <svg viewBox="0 0 30 30" fill="none" stroke="#fff" stroke-width="1.5"><path d="M19 4a11 11 0 1 1 0 22"/><path d="M4 15h18M17 10l5 5-5 5"/></svg></a>
  </article>

  <article class="card" style="left:771px">
    <svg class="icon" viewBox="0 0 66 66" fill="none" stroke="#222" stroke-width="1.8"><rect x="6" y="38" width="56" height="16" rx="2"/><path d="M50 38V8M54 38V8M50 8h4"/><circle cx="14" cy="46" r="2"/><circle cx="21" cy="46" r="2"/><circle cx="28" cy="46" r="2"/><path d="M36 46h10M10 54v4M58 54v4"/><path d="M14 30a16 16 0 0 1 22 0M18 34a9 9 0 0 1 14 0M10 26a22 22 0 0 1 30 0"/></svg>
    <h3>BXN Relay</h3>
    <p>"Advanced integration to optimize plant communication."</p>
    <a class="more">Learn More <svg viewBox="0 0 30 30" fill="none" stroke="#222" stroke-width="1.5"><path d="M19 4a11 11 0 1 1 0 22"/><path d="M4 15h18M17 10l5 5-5 5"/></svg></a>
  </article>
</section>

<section>
  <svg class="why-bg" width="1200" height="620" viewBox="0 0 1200 620">
    <polygon points="0,7 404,63 0,87" fill="var(--grey)"/>
    <polygon points="0,113 1200,23 1200,512 0,584" fill="var(--blue)"/>
    <polygon points="800,562 1200,529 1200,616" fill="var(--grey)"/>
  </svg>
  <div class="why-photo" role="img" aria-label="Two engineers in hard hats and safety vests shaking hands in a warehouse"></div>
  <div class="why-copy">
    <div class="bar"></div>
    <h2>Why Datavane <span>Is Your Strategic Ally</span></h2>
    <ul>
      <li><svg viewBox="0 0 16 16"><circle cx="8" cy="8" r="8" fill="#fff"/><path d="M4 8h7M8 5l3 3-3 3" stroke="var(--blue)" stroke-width="1.8" fill="none"/></svg>Over 20 years of experience in industrial solutions.</li>
      <li><svg viewBox="0 0 16 16"><circle cx="8" cy="8" r="8" fill="#fff"/><path d="M4 8h7M8 5l3 3-3 3" stroke="var(--blue)" stroke-width="1.8" fill="none"/></svg>Team of experts in connectivity and automation.</li>
      <li><svg viewBox="0 0 16 16"><circle cx="8" cy="8" r="8" fill="#fff"/><path d="M4 8h7M8 5l3 3-3 3" stroke="var(--blue)" stroke-width="1.8" fill="none"/></svg>Personalized technical support.</li>
    </ul>
  </div>
</section>

<section>
  <div class="rule" style="left:527px;top:2042px;width:146px"></div>
  <h2 class="sec-title" style="top:2062px">Success <span>Stories</span></h2>
  <div class="quote-mark" style="left:108px;top:2146px">&#8220;</div>
  <p class="quote-text">Lorem ipsum dolor sit amet, consectetur adipiscing elit, sed do eiusmod tempor incididunt ut labore et dolore magna aliqua. Ut enim ad minim veniam, quis nostrud exercitation ullamco laboris nisi ut aliquip ex ea commodo consequat.</p>
  <div class="quote-mark" style="left:588px;top:2310px">&#8221;</div>
  <div class="author"><span class="name">Marek Lind</span><span class="role">Production Engineer</span></div>
  <div class="dots"><i class="on"></i><i></i><i></i><i></i></div>
  <div class="portrait-ring"></div>
  <div class="portrait" role="img" aria-label="Portrait of a smiling engineer in a dark blazer seated at a desk"></div>
</section>

<footer>
  <svg class="foot-bg" width="1200" height="839" viewBox="0 0 1200 839">
    <polygon points="0,10 418,70 0,94" fill="var(--blue)"/>
    <polygon points="0,120 1200,27 1200,839 0,839" fill="var(--black)"/>
  </svg>
  <div class="cta-copy">
    <div class="bar"></div>
    <h2>Ready to Transform<br>Your Plant?</h2>
    <p>Lorem ipsum dolor sit amet, consectetur adipiscing elit, sed do eiusmod tempor incididunt ut labore et dolore magna aliqua. Ut enim ad minim veniam, quis nostrud exercitation ullamco laboris nisi ut aliquip ex ea commodo consequat. Duis aute irure dolor in reprehenderit in voluptate velit esse cillum dolore eu fugiat nulla pariatur</p>
  </div>
  <a class="btn solid cta">Schedule a Demo or Consultation.
    <svg viewBox="0 0 26 26" fill="none" stroke="#fff" stroke-width="1.5"><path d="M17 4a10 10 0 1 1 0 18"/><path d="M4 13h15M14 8l5 5-5 5"/></svg></a>
  <div class="foot-brand">Datavane</div>
  <div class="copyright">Copyright © 2025 Datavane | &nbsp;All Rights Reserved</div>

  <form class="form-card">
    <h3>Get In Touch</h3>
    <div class="field" style="top:87px">Name</div>
    <div class="field" style="top:154px">Email</div>
    <div class="field" style="top:222px">Company</div>
    <div class="field" style="top:290px">Phone</div>
    <div class="field" style="top:357px;height:132px">Message</div>
    <div class="send">Send Now <svg viewBox="0 0 28 28" fill="none" stroke="#fff" stroke-width="1.5"><path d="M18 4a10 10 0 1 1 0 20"/><path d="M5 14h16M16 9l5 5-5 5"/></svg></div>
  </form>
</footer>

</body>
</html>
```